Changes to wine label

Need existing labels designed by Pixel Harbor corrected to meet QRV.

Target Market(s)

Wine drinkers

Requirements
Must have
• Use attached label design. A. Label #2 spelling correct" Zinfandel". Also, 500ml instead of 375ml and place on front label with so would be 500ml/Alcohol %18 By Volume. Remove residual sugar text.
Should not have
• Sorrel Bluff LOGO on both label#1 & #2 different red that pops the log. And an addtional label with the white grapes

```html
<!DOCTYPE html>
<html lang="en">
<head>
<meta charset="utf-8">
<title>Sorrel Bluff Mead Co – Wine Labels</title>
<link rel="stylesheet" href="https://fonts.googleapis.com/css2?family=Cinzel:wght@500&family=Noto+Serif:wght@400;700&family=Source+Sans+3:ital,wght@0,400;0,700;1,400&display=swap">
<style>
  :root {
    --backdrop: #b09a55;
    --label-black: #050505;
    --label-glow: #2a2a2a;
    --brand-red: #e0201c;
    --text-white: #ffffff;
    --text-soft: #e8e8e8;
    --seal-gold: #c9a94a;
    --grape-gold: #e8a61f;
    --grape-ember: #c0491a;
    --grape-plum: #b65ca8;
    --grape-wine: #7d2e72;
  }
  * { box-sizing: border-box; margin: 0; padding: 0; }
  html, body { width: 1200px; height: 1200px; overflow: hidden; }
  body { background: var(--backdrop); position: relative; }

  .label {
    position: absolute;
    width: 436px;
    height: 523px;
    background: radial-gradient(ellipse at 50% 55%, var(--label-glow) 0%, var(--label-black) 62%);
    box-shadow: 4px 6px 12px rgba(0,0,0,.35);
    color: var(--text-white);
    text-align: center;
  }
  .label--front-gold  { left: 137px; top: 58px; }
  .label--back-gold   { left: 628px; top: 58px; }
  .label--front-plum  { left: 137px; top: 620px; }
  .label--back-plum   { left: 628px; top: 620px; }

  .brand-name {
    position: absolute;
    left: 0; right: 0;
    font-family: "Cinzel", serif;
    font-weight: 500;
    color: var(--brand-red);
    letter-spacing: 3px;
    white-space: nowrap;
  }
  .label--front .brand-name { top: 106px; font-size: 30px; line-height: 32px; }
  .label--back .brand-name  { top: 70px;  font-size: 21px; line-height: 23px; }

  .grape-art {
    position: absolute;
    left: 106px; top: 196px;
    width: 222px; height: 228px;
    border-radius: 45% 55% 50% 50% / 40% 40% 60% 60%;
  }
  .grape-art--gold { background: radial-gradient(circle at 45% 40%, var(--grape-gold), var(--grape-ember) 85%); }
  .grape-art--plum { background: radial-gradient(circle at 45% 40%, var(--grape-plum), var(--grape-wine) 85%); }

  .volume-line {
    position: absolute;
    left: 0; right: 0; top: 472px;
    font-family: "Source Sans 3", sans-serif;
    font-size: 13px;
    line-height: 16px;
  }

  .varietal {
    position: absolute;
    left: 0; right: 0; top: 131px;
    font-family: "Noto Serif", serif;
    font-weight: 700;
    font-size: 14px;
    line-height: 15.5px;
  }
  .tasting-note {
    position: absolute;
    left: 0; right: 0; top: 173px;
    font-family: "Noto Serif", serif;
    font-size: 17px;
    line-height: 18.5px;
    white-space: nowrap;
  }
  .producer {
    position: absolute;
    left: 0; right: 0; top: 305px;
    font-family: "Source Sans 3", sans-serif;
    font-style: italic;
    font-size: 10.5px;
    line-height: 14.5px;
    color: var(--text-soft);
  }
  .warning {
    position: absolute;
    left: 22px; top: 352px;
    text-align: left;
    font-family: "Source Sans 3", sans-serif;
    font-size: 13.5px;
    line-height: 18px;
    white-space: nowrap;
  }
  .warning strong { font-weight: 700; }
  .fine-print {
    position: absolute;
    left: 22px; right: 32px; top: 444px;
    display: flex;
    justify-content: space-between;
    font-family: "Source Sans 3", sans-serif;
    font-size: 11px;
    line-height: 14px;
  }
  .seal {
    position: absolute;
    left: 187px; top: 451px;
    width: 53px; height: 53px;
    border-radius: 50%;
    background: radial-gradient(circle at 40% 35%, #e8cf7a, var(--seal-gold) 70%);
  }
</style>
</head>
<body>

  <section class="label label--front label--front-gold">
    <div class="brand-name">Sorrel Bluff<br>Mead Co</div>
    <div class="grape-art grape-art--gold" role="img" aria-label="Painted illustration of a bunch of golden white grapes"></div>
    <p class="volume-line">500ML / ALCOHOL 18% BY VOLUME</p>
  </section>

  <section class="label label--back label--back-gold">
    <div class="brand-name">Sorrel Bluff<br>Mead Co</div>
    <p class="varietal">CALIFORNIA<br>ZINFANDEL 50% SYRAH 50%</p>
    <p class="tasting-note">A fruit forward dessert style wine that<br>takes the aroma of the varitals and balances<br>it with sweetness and zealous acidity.<br>Meant to be drunk young or slightly aged,<br>complementary with cheeses and chocolate.</p>
    <p class="producer">PRODUCED AND BOTTLED BY<br>SORREL BLUFF MEAD CO. LARKWOOD, CALDERA VALLEY</p>
    <p class="warning"><strong>GOVERNMENT WARNING:</strong> (1) According to the Surgeon<br>General, women should not drink alcoholic beverages during<br>pregnancy because of the risk of birth defects. (2) Consumption<br>of alcoholic beverages impairs your ability to drive a car or<br>operate machinery, and may cause health problems.</p>
    <div class="fine-print"><span>500ML</span><span>CONTAINS SULFITES</span></div>
    <div class="seal"></div>
  </section>

  <section class="label label--front label--front-plum">
    <div class="brand-name">Sorrel Bluff<br>Mead Co</div>
    <div class="grape-art grape-art--plum" role="img" aria-label="Painted illustration of a bunch of purple red grapes"></div>
    <p class="volume-line">500ML / ALCOHOL 18% BY VOLUME</p>
  </section>

  <section class="label label--back label--back-plum">
    <div class="brand-name">Sorrel Bluff<br>Mead Co</div>
    <p class="varietal">CALIFORNIA<br>ZINFANDEL 50% SYRAH 50%</p>
    <p class="tasting-note">A fruit forward dessert style wine that<br>takes the aroma of the varitals and balances<br>it with sweetness and zealous acidity.<br>Meant to be drunk young or slightly aged,<br>complementary with cheeses and chocolate.</p>
    <p class="producer">PRODUCED AND BOTTLED BY<br>SORREL BLUFF MEAD CO. LARKWOOD, CALDERA VALLEY</p>
    <p class="warning"><strong>GOVERNMENT WARNING:</strong> (1) According to the Surgeon<br>General, women should not drink alcoholic beverages during<br>pregnancy because of the risk of birth defects. (2) Consumption<br>of alcoholic beverages impairs your ability to drive a car or<br>operate machinery, and may cause health problems.</p>
    <div class="fine-print"><span>500ML</span><span>CONTAINS SULFITES</span></div>
    <div class="seal"></div>
  </section>

</body>
</html>
```